Design eBook Cover for Homeowner Association (HOA) book

We need a cover design for an eBook entitled "The Residents Council Leader's Manual: Practical Steps and Proven Methods".

Title: The Residents Council Leader's Manual

Subtitle: Practical Steps and Proven Methods

Name of Author: Gerald Whitcombe, CMA

Style: Professional Guide

Testimonial: "This book is an indispensable tool for anyone on an HOA board. The expert advice and practical approach in 'The Residents Council Leader's Manual' have made a world of difference in our community. Every board member should have a copy!"
— Marla Quint, HOA Board President

I have uploaded a file as design inspiration but not locked into the colors or look. Just want a clean, professional looking cover.

Target Market(s)

Board members of HOAs (Homeowners associations) in the United States

Industry/Entity Type

Real Estate, HOA

Requirements
Must have
• Clean, professional appearance that conveys authority

```html
<!DOCTYPE html>
<html lang="en">
<head>
<meta charset="utf-8">
<title>The Residents Council Leader's Manual — Cover</title>
<link rel="stylesheet" href="https://fonts.googleapis.com/css2?family=Arimo:wght@400;700&display=swap">
<style>
  :root {
    --page: #ffffff;
    --cover-blue: #38aff0;
    --ink-navy: #0b1f4b;
    --ink-white: #ffffff;
    --rule: #e8f6ff;
    --emblem-fill: #8fd1f7;
  }
  html, body {
    margin: 0;
    padding: 0;
    width: 1200px;
    height: 1200px;
    overflow: hidden;
    background: var(--page);
    font-family: "Arimo", Arial, sans-serif;
  }
  .canvas {
    position: relative;
    width: 1200px;
    height: 1200px;
  }
  .cover {
    position: absolute;
    left: 262px;
    top: 45px;
    width: 750px;
    height: 1110px;
    background: var(--cover-blue);
  }
  .testimonial {
    position: absolute;
    left: 300px;
    top: 103px;
    width: 680px;
    margin: 0;
    text-align: center;
    color: var(--ink-white);
    font-size: 14.5px;
    line-height: 20px;
    letter-spacing: 0.2px;
  }
  .testimonial-source {
    position: absolute;
    left: 300px;
    top: 169px;
    width: 680px;
    margin: 0;
    text-align: center;
    color: var(--ink-navy);
    font-weight: 700;
    font-size: 15px;
  }
  .title-art {
    position: absolute;
    left: 0;
    top: 0;
    width: 1200px;
    height: 1200px;
  }
  .title-light { fill: var(--ink-white); font-family: "Arimo", Arial, sans-serif; font-weight: 400; }
  .title-bold { fill: var(--ink-navy); font-family: "Arimo", Arial, sans-serif; font-weight: 700; }
  .house-emblem {
    position: absolute;
    left: 722px;
    top: 270px;
    width: 212px;
    height: 192px;
    background: var(--emblem-fill);
  }
  .subtitle-rule {
    position: absolute;
    left: 346px;
    width: 587px;
    height: 2px;
    background: var(--rule);
  }
  .subtitle-rule.top { top: 856px; }
  .subtitle-rule.bottom { top: 984px; }
  .subtitle {
    position: absolute;
    left: 330px;
    top: 866px;
    width: 620px;
    margin: 0;
    text-align: center;
    color: var(--ink-navy);
    font-size: 44px;
    line-height: 54px;
    font-weight: 400;
  }
  .author {
    position: absolute;
    left: 330px;
    top: 1053px;
    width: 620px;
    margin: 0;
    text-align: center;
    color: var(--ink-white);
    font-size: 39px;
    letter-spacing: 1.5px;
    white-space: nowrap;
  }
  .author-name { font-weight: 700; }
  .author-credential { font-weight: 400; }
</style>
</head>
<body>
<main class="canvas">
  <section class="cover"></section>

  <p class="testimonial">" This book is an indispensable tool for anyone on an HOA board. The expert advice<br>and practical approach in 'The Residents Council Leader's Manual' have made a world of<br>difference in our community. Every board member should have a copy! "</p>
  <p class="testimonial-source">— Marla Quint, HOA Board President</p>

  <svg class="title-art" viewBox="0 0 1200 1200" aria-label="The Residents Council Leader's Manual">
    <text class="title-light" x="348" y="465" font-size="250" textLength="360" lengthAdjust="spacingAndGlyphs">THE</text>
    <text class="title-bold" x="348" y="597" font-size="122" textLength="585" lengthAdjust="spacingAndGlyphs">RESIDENTS</text>
    <text class="title-bold" x="348" y="708" font-size="122" textLength="585" lengthAdjust="spacingAndGlyphs">COUNCIL</text>
    <text class="title-light" x="348" y="797" font-size="76" textLength="585" lengthAdjust="spacingAndGlyphs">LEADER'S MANUAL</text>
  </svg>

  <div class="house-emblem" role="img" aria-label="White outline house icon with a double roofline and small window"></div>

  <div class="subtitle-rule top"></div>
  <p class="subtitle">Practical Steps and<br>Proven Methods</p>
  <div class="subtitle-rule bottom"></div>

  <p class="author"><span class="author-name">GERALD WHITCOMBE,</span> <span class="author-credential">CMA</span></p>
</main>
</body>
</html>
```